Project Brief: Bright Lane Works Business Card Design

I’m looking for a modern, monochromatic business card design (black and white only) that reflects the sophistication and intelligence of my company, Bright Lane Works (www.brightlaneworks.example) — a firm that helps small and medium-sized businesses automate operations and integrate AI into their workflows.

The design should communicate clarity, confidence, and innovation — clean and minimal, yet bold and professional.

Design Direction
-Color: Monochrome palette — black, white, and shades of gray only.
-Design should support matte or soft-touch finish.
-Optional: include mockups showing foil or embossed variations

Layout Concept:
-Ideally, one side white and the other black for contrast.
-Horizontal Orientation 2" x 3.5"

Typography:
-Use clean, geometric sans-serifs (e.g., Inter, Poppins, Helvetica Neue, DM Sans, etc.).

Front Side (Brand Side)
-Prominently feature the Bright Lane Works logo & Tag line(attached).

Back Side (Personal Side)

Include:
-Marcus Whitaker
-Founder
-mwhitaker@brightlaneworks.example
-www.brightlaneworks.example
-Office: 555.214.3386
-Mobile: 555.281.4472
-Add a QR code that links directly to my LinkedIn profile (bottom right corner preferred). Maintain strong visual balance and readability — the QR should feel integrated, not like an afterthought.

Target Market(s)

Small/Medium Sized Business Owners

Industry/Entity Type

Consulting

Contact Information for Business Card

See Project Description

Font styles to use
Sans Serif

Colors

Designer to choose only greyscale colors for use in the design.

Requirements
Must have
• See Project Description
Nice to have
• See Project Description
Should not have
• See Project Description

```html
<!DOCTYPE html>
<html lang="en">
<head>
<meta charset="utf-8">
<title>Bright Lane Works — Business Card</title>
<link rel="stylesheet" href="https://fonts.googleapis.com/css2?family=Outfit:wght@400;600&family=Montserrat:wght@400;700&display=swap">
<style>
  :root {
    --page: #e4e4e4;
    --white: #ffffff;
    --ink: #111111;
    --panel: #141414;
    --silver-light: #f2f2f2;
    --silver-mid: #a9a9a9;
    --silver-dark: #5c5c5c;
    --mark-grey: #c4c4c4;
  }
  * { margin: 0; padding: 0; box-sizing: border-box; }
  html, body { width: 1200px; height: 1200px; overflow: hidden; }
  body { background: var(--page); position: relative; }

  .card {
    position: absolute;
    left: 152px;
    width: 896px;
    height: 524px;
  }
  .card--front { top: 54px; background: var(--white); }
  .card--back  { top: 621px; background: var(--ink); }

  .brand { position: absolute; display: flex; align-items: center; gap: 22px; }
  .brand__text { display: flex; flex-direction: column; align-items: flex-end; }
  .brand__name {
    font-family: "Outfit", sans-serif;
    font-weight: 600;
    font-size: 66px;
    line-height: 1;
    letter-spacing: -0.5px;
    white-space: nowrap;
  }
  .brand__tagline {
    margin-top: 18px;
    font-family: "Outfit", sans-serif;
    font-weight: 400;
    font-size: 21px;
    letter-spacing: 0.22em;
    margin-right: -0.22em;
    white-space: nowrap;
  }
  .brand__square { width: 96px; height: 96px; flex: none; }

  .card--front .brand { left: 84px; top: 72px; color: var(--ink); }
  .card--front .brand__square { background: var(--ink); }

  .card--back .brand { left: 50%; top: 50%; transform: translate(-50%, -50%); color: var(--white); }
  .card--back .brand__square { background: var(--mark-grey); }

  .person { position: absolute; left: 60px; top: 360px; }
  .person__name {
    font-family: "Montserrat", sans-serif;
    font-weight: 700;
    font-size: 25px;
    letter-spacing: 0.02em;
    color: var(--ink);
  }
  .person__role {
    margin-top: 4px;
    font-family: "Montserrat", sans-serif;
    font-weight: 400;
    font-size: 24px;
    color: var(--ink);
  }

  .contact {
    position: absolute;
    left: 421px;
    top: 295px;
    width: 475px;
    height: 199px;
    background: var(--panel);
    padding: 20px 0 0 62px;
  }
  .contact::before {
    content: "";
    position: absolute;
    left: 0; top: 0; bottom: 0;
    width: 12px;
    background: linear-gradient(90deg, var(--silver-dark), var(--silver-light) 45%, var(--silver-mid));
  }
  .contact__list { list-style: none; }
  .contact__item {
    display: flex;
    align-items: center;
    height: 41.5px;
    font-family: "Montserrat", sans-serif;
    font-size: 18.5px;
    color: var(--white);
    white-space: nowrap;
  }
  .contact__icon { width: 18px; height: 18px; margin-right: 14px; flex: none; fill: var(--white); }
</style>
</head>
<body>

<section class="card card--front" aria-label="Business card, personal side">
  <div class="brand">
    <div class="brand__text">
      <div class="brand__name">Bright Lane Works</div>
      <div class="brand__tagline">INTELLIGENT AUTOMATION</div>
    </div>
    <div class="brand__square"></div>
  </div>

  <div class="person">
    <div class="person__name">MARCUS WHITAKER</div>
    <div class="person__role">Founder</div>
  </div>

  <div class="contact">
    <ul class="contact__list">
      <li class="contact__item">
        <svg class="contact__icon" viewBox="0 0 24 24" aria-hidden="true"><path d="M6.6 10.8a15.1 15.1 0 0 0 6.6 6.6l2.2-2.2c.3-.3.7-.4 1-.2 1.1.4 2.3.6 3.6.6.6 0 1 .4 1 1V20c0 .6-.4 1-1 1A17 17 0 0 1 3 4c0-.6.4-1 1-1h3.5c.6 0 1 .4 1 1 0 1.3.2 2.5.6 3.6.1.3 0 .7-.2 1z"/></svg>
        555.214.3386
      </li>
      <li class="contact__item">
        <svg class="contact__icon" viewBox="0 0 24 24" aria-hidden="true"><path d="M8 2h8a2 2 0 0 1 2 2v16a2 2 0 0 1-2 2H8a2 2 0 0 1-2-2V4a2 2 0 0 1 2-2zm0 3v13h8V5zm4 14.2a.9.9 0 1 0 0 1.8.9.9 0 0 0 0-1.8z"/></svg>
        555.281.4472
      </li>
      <li class="contact__item">
        <svg class="contact__icon" viewBox="0 0 24 24" aria-hidden="true"><path d="M3 5h18a1 1 0 0 1 1 1v12a1 1 0 0 1-1 1H3a1 1 0 0 1-1-1V6a1 1 0 0 1 1-1zm1 2.5V17h16V7.5l-8 5z"/><path d="M4 6.5l8 5 8-5z"/></svg>
        mwhitaker@brightlaneworks.example
      </li>
      <li class="contact__item">
        <svg class="contact__icon" viewBox="0 0 24 24" aria-hidden="true"><path d="M12 2a10 10 0 1 0 0 20 10 10 0 0 0 0-20zm6.9 9h-3a15 15 0 0 0-1.3-5.9A8 8 0 0 1 18.9 11zM12 4.1c.9 1.2 1.8 3.6 1.9 6.9h-3.8c.1-3.3 1-5.7 1.9-6.9zM9.4 5.1A15 15 0 0 0 8.1 11h-3a8 8 0 0 1 4.3-5.9zM5.1 13h3a15 15 0 0 0 1.3 5.9A8 8 0 0 1 5.1 13zm6.9 6.9c-.9-1.2-1.8-3.6-1.9-6.9h3.8c-.1 3.3-1 5.7-1.9 6.9zm2.6-1a15 15 0 0 0 1.3-5.9h3a8 8 0 0 1-4.3 5.9z"/></svg>
        www.brightlaneworks.example
      </li>
    </ul>
  </div>
</section>

<section class="card card--back" aria-label="Business card, brand side">
  <div class="brand">
    <div class="brand__text">
      <div class="brand__name">Bright Lane Works</div>
      <div class="brand__tagline">INTELLIGENT AUTOMATION</div>
    </div>
    <div class="brand__square"></div>
  </div>
</section>

</body>
</html>
```